ZEH Project Signage

Need a sign to be displayed in the front of properties currently under Construction or Renovation to advertise our company information. Need it to be Professional and Contemporary. We are a Design/Build Construction Company. Information should include Company Name, email, website, phone number. Attached: Logo and company brochure, also included and inspiration images

```html
<!DOCTYPE html>
<html lang="en">
<head>
<meta charset="utf-8">
<title>ZEH Project Signage</title>
<link href="https://fonts.googleapis.com/css2?family=Anton&family=Montserrat:wght@400;500;700&display=swap" rel="stylesheet">
<style>
  :root {
    --backdrop: #f1f1f1;
    --sign-white: #ffffff;
    --ink: #0a0a0a;
    --signal-yellow: #eeeb3d;
    --reverse-white: #ffffff;
  }
  * { margin: 0; padding: 0; box-sizing: border-box; }
  html, body {
    width: 1200px; height: 1200px; overflow: hidden;
    background: var(--backdrop);
  }
  .sign {
    position: absolute; left: 231px; top: 49px;
    width: 737px; height: 1102px;
    background: var(--sign-white);
    overflow: hidden;
    font-family: 'Montserrat', sans-serif;
    color: var(--ink);
  }
  .brand {
    position: absolute; left: 0; top: 128px; width: 100%;
    display: flex; justify-content: center; align-items: center; gap: 18px;
  }
  .brand-name {
    font-family: 'Montserrat', sans-serif;
    font-weight: 500; font-size: 40px; letter-spacing: 3px;
    color: var(--ink); white-space: nowrap;
  }
  .brand-dot {
    width: 40px; height: 40px; border-radius: 50%;
    border: 6px solid var(--signal-yellow);
  }
  .headline {
    position: absolute; left: 0; width: 100%;
    text-align: center;
    font-family: 'Anton', sans-serif;
    font-weight: 400;
    line-height: 1; color: var(--ink);
    white-space: nowrap;
  }
  .headline-short { top: 436px; font-size: 102px; letter-spacing: 4px; }
  .headline-long { top: 541px; font-size: 120px; letter-spacing: 6px; }
  .contact-line {
    position: absolute; left: 62px;
    display: flex; align-items: center; gap: 24px;
    font-size: 37px; font-weight: 400; white-space: nowrap;
  }
  .contact-line svg { width: 32px; height: 32px; flex: none; }
  .contact-email { top: 700px; }
  .contact-web { top: 756px; }
  .phone-band {
    position: absolute; left: 0; top: 0;
    width: 737px; height: 1102px;
  }
  .phone-row {
    position: absolute; left: 0; width: 100%;
    text-align: center; color: var(--reverse-white);
    font-size: 50px; font-weight: 400; white-space: nowrap;
  }
  .phone-row strong { font-weight: 700; }
  .phone-direct { top: 937px; }
  .phone-office { top: 1022px; }
</style>
</head>
<body>
  <main class="sign">
    <div class="brand">
      <span class="brand-name">ZEH CONSTRUCTION</span>
      <span class="brand-dot"></span>
    </div>

    <h1 class="headline headline-short">ZEH</h1>
    <h2 class="headline headline-long">Construction</h2>

    <p class="contact-line contact-email">
      <svg viewBox="0 0 32 32" fill="none" stroke="#0a0a0a" stroke-width="2.2">
        <rect x="3" y="9" width="26" height="19"/>
        <path d="M3 9 L16 19 L29 9 M3 28 L13 17 M29 28 L19 17"/>
        <path d="M8 9 V4 H24 V9"/>
      </svg>
      marc@zehconstruction.com
    </p>
    <p class="contact-line contact-web">
      <svg viewBox="0 0 32 32" fill="none" stroke="#0a0a0a" stroke-width="2.2">
        <circle cx="16" cy="16" r="13"/>
        <ellipse cx="16" cy="16" rx="6" ry="13"/>
        <path d="M3 16 H29 M5 9 H27 M5 23 H27 M16 3 V29"/>
      </svg>
      www.zehconstruction.com
    </p>

    <svg class="phone-band" viewBox="0 0 737 1102">
      <path d="M0 905 H737 V1102 H0 Z" fill="var(--signal-yellow)"/>
      <path d="M0 1020 Q368 578 737 1020 V1102 H0 Z" fill="var(--signal-yellow)"/>
      <path d="M0 1032 Q368 594 737 1032 V1102 H0 Z" fill="var(--ink)"/>
      <line x1="242" y1="878" x2="307" y2="878" stroke="var(--signal-yellow)" stroke-width="3"/>
      <line x1="435" y1="878" x2="500" y2="878" stroke="var(--signal-yellow)" stroke-width="3"/>
      <circle cx="370" cy="870" r="42" fill="none" stroke="var(--signal-yellow)" stroke-width="4"/>
      <path d="M352 848 c4 -2 8 -1 10 3 l4 8 c1 3 0 6 -3 8 l-3 2 c3 7 8 12 15 15 l2 -3 c2 -3 5 -4 8 -3 l8 4 c4 2 5 6 3 10 c-3 6 -9 8 -15 6 c-15 -5 -27 -17 -32 -32 c-2 -6 0 -12 3 -18 z" fill="var(--signal-yellow)"/>
      <path d="M376 852 a14 14 0 0 1 12 12 M377 843 a22 22 0 0 1 20 20 M378 834 a30 30 0 0 1 28 28" fill="none" stroke="var(--signal-yellow)" stroke-width="3" stroke-linecap="round"/>
      <line x1="94" y1="1012" x2="643" y2="1012" stroke="var(--signal-yellow)" stroke-width="4"/>
    </svg>

    <p class="phone-row phone-direct">Direct: <strong>561.555.0142</strong></p>
    <p class="phone-row phone-office">Office: <strong>561.555.0178</strong></p>
  </main>
</body>
</html>
```